Aquatic View

We need a web design for a new window cleaning company name Tidal Pane Care. We are located in Grand Cayman, Cayman Islands. We are a small company, a team of husband and wife. Our services include residencial interior and exterior window cleaning and commercial. Extra services such as ceiling fans cleaning, mirrors, high dusting. Home cleaning services. Power washing. Explaining the service. We want a modern, beachy style with aquatic colors. We want to use our domain name "tidalpanecare.ky". We want to portray a clean, modern and professional design.

Target Market(s)

Big Home owners

Industry/Entity Type

Cleaning Service

Contact Information for Business Card

Company Name: Tidal Pane Care
Name: Dennis Okafor owner/manager
Phone: 345-5550194
Email: dennis@tidalpanecare.ky
Website: tidalpanecare.ky
Address: P.O.Box 4820 GT, George Town, Grand Cayman KY1-2043 Cayman Islands

Number of Pages Required

2 page

Font styles to use
Sans Serif

Colors
0592cd
0455a3
33a6d7
85cae6
cadf82
abd036
fbf289

Requirements
Nice to have
• Pictures of an ocean view and palm trees from clear windows.
• https://quelvaro.com/bidmatic/
• Use the above for "free estimate".

```html
<!DOCTYPE html>
<html lang="en">
<head>
<meta charset="utf-8">
<title>Tidal Pane Care</title>
<link href="https://fonts.googleapis.com/css2?family=Antic+Slab&family=Open+Sans:wght@400;600&family=PT+Sans:ital,wght@0,400;0,700;1,400&display=swap" rel="stylesheet">
<style>
:root{
  --ocean:#0592cd;
  --deep:#0455a3;
  --sky:#33a6d7;
  --mist:#85cae6;
  --lime:#abd036;
  --lime-soft:#cadf82;
  --heading:#1d4f8a;
  --text:#555;
  --line:#e2e2e2;
  --panel:#f4f4f4;
}
*{box-sizing:border-box;margin:0;padding:0}
html,body{width:960px;height:1200px;overflow:hidden;background:#fff}
body{position:relative;font-family:"PT Sans",sans-serif;color:var(--text)}
.abs{position:absolute}
.top-rule{left:155px;top:0;width:665px;height:2px;background:var(--ocean)}
.corner-tab{left:808px;top:0;width:12px;height:14px}
.top-bar{left:216px;top:7px;font-size:5.5px;color:#666}
.top-divider{left:155px;top:20px;width:665px;height:1px;background:var(--line)}
.brand{left:216px;top:40px;display:flex;align-items:center;gap:6px}
.brand-mark{width:20px;height:20px;background:var(--ocean)}
.brand-name{font-family:"Open Sans",sans-serif;font-weight:600;font-size:16px;color:var(--deep);letter-spacing:-.2px}
.nav{top:34px;height:14px;font-family:"Antic Slab",serif;font-size:7.5px;color:#444}
.nav a{position:absolute;top:0;color:inherit;text-decoration:none;white-space:nowrap}
.nav a.current{color:var(--ocean)}
.nav a.current::before{content:"";position:absolute;left:0;right:0;top:-14px;height:1.5px;background:var(--ocean)}
.hero{left:155px;top:86px;width:665px;height:172px;overflow:hidden;
  background:linear-gradient(180deg,#7fd3f4 0%,#3ab4e6 35%,#1b7fc0 55%,#e9ecef 62%,#cfd4d8 100%)}
.hero-title{left:59px;top:34px;width:240px;font-family:"Open Sans",sans-serif;font-weight:600;font-size:17px;line-height:22px;color:#fff;text-shadow:0 1px 3px rgba(0,0,0,.45)}
.hero-btn{left:59px;top:136px;width:101px;height:28px;background:var(--lime);color:#fff;font-family:"Antic Slab",serif;font-size:11px;display:flex;align-items:center;justify-content:center}
.section-title{left:0;width:960px;text-align:center;font-family:"Antic Slab",serif;color:var(--heading);font-size:16.5px}
.section-sub{left:0;width:960px;text-align:center;font-family:"Antic Slab",serif;color:#333;font-size:10.5px}
.about-photo{left:218px;top:334px;width:123px;height:76px;background:linear-gradient(135deg,#e9f3fa,#b9d7ea 60%,#f0a74a 62%,#dbe9f3 70%);box-shadow:0 1px 3px rgba(0,0,0,.2)}
.about-copy{left:356px;top:333px;width:382px;font-size:6.2px;line-height:8.8px;color:#666}
.about-copy p{margin-bottom:8.5px}
.read-more{left:356px;top:413px;font-size:6.2px;color:var(--deep)}
.consult{left:210px;top:443px;width:557px;height:325px;overflow:hidden;
  background:linear-gradient(180deg,#1f5fb0 0%,#3b7fc7 30%,#5ba2d9 55%,#8ac8e4 75%,#a8dcec 100%)}
.consult-title{left:0;top:22px;width:557px;text-align:center;font-family:"Antic Slab",serif;font-size:16.5px;color:#fff}
.consult-sub{left:0;top:52px;width:557px;text-align:center;font-family:"Antic Slab",serif;font-size:10.5px;color:#fff}
.consult-arrow{left:262px;top:77px}
.form-card{left:131px;top:124px;width:295px;height:170px;background:#fff;border-radius:9px}
.field{position:absolute;left:9px;width:276px;height:13px;border:1px solid #d6d6d6;font-size:5.8px;color:#aaa;padding:2px 6px;font-family:"PT Sans",sans-serif}
.field.select{padding-left:10px}
.field.select::after{content:"";position:absolute;right:0;top:0;width:14px;height:11px;border-left:1px solid #d6d6d6}
.field.area{height:40px}
.send-btn{position:absolute;width:47px;height:20px;background:linear-gradient(#8ecdec,#4fa7d8);color:var(--deep);font-size:6px;font-weight:700;display:flex;align-items:center;justify-content:center;border-radius:1px}
.testimonials{left:210px;top:782px;width:557px;height:187px;background:var(--panel)}
.avatar{position:absolute;border-radius:50%;background:radial-gradient(circle at 45% 40%,#d9b9a0,#9db6cf 60%,#c9d9e8)}
.quote{left:73px;top:82px;width:445px;font-size:7px;line-height:9px;font-style:italic;color:#888}
.quote-role{left:73px;top:108px;font-size:7px;font-style:italic;color:#888}
.quote-author{left:440px;top:124px;font-size:6px;font-style:italic;color:var(--ocean)}
.quote-bar{left:526px;top:80px;width:2px;height:36px;background:var(--deep)}
.slide-btn{position:absolute;width:14px;height:14px;border-radius:50%;background:#8d8d8d;opacity:.85}
.dot{position:absolute;width:4.5px;height:4.5px;border-radius:50%;background:#777}
.dot.on{background:#111}
.footer-gap{left:155px;top:995px;width:665px;height:5px;background:#ececec}
.footer{left:155px;top:1000px;width:665px;height:170px;background:var(--deep);color:#fff}
.footer-head{position:absolute;top:22px;font-size:6.8px;letter-spacing:.2px;font-family:"PT Sans",sans-serif}
.menu a{position:absolute;left:61px;width:170px;font-size:6.2px;color:#fff;text-decoration:none;padding-bottom:6px;border-bottom:1px solid rgba(255,255,255,.12)}
.menu a.current{color:#2e7fc7}
.contact-lines{left:247px;top:39px;font-size:6.2px;line-height:8.8px}
.foot-field{position:absolute;left:433px;width:171px;height:12px;background:#fff;font-size:5.8px;color:#aaa;padding:2px 4px;border:1px solid #cfcfcf}
.bottom-bar{left:155px;top:1170px;width:665px;height:30px;background:var(--ocean);color:#fff}
.copyright{left:61px;top:11px;font-size:5.8px}
.social{position:absolute;top:12px;width:7px;height:7px;border-radius:50%;background:#fff}
.to-top{left:627px;top:15px;width:24px;height:15px;background:#1b3a5c;border-radius:2px 2px 0 0}
</style>
</head>
<body>
  <div class="abs top-rule"></div>
  <svg class="abs corner-tab" viewBox="0 0 12 14" aria-hidden="true"><polygon points="0,0 12,0 12,14" fill="#333"/><path d="M8 2.5v4M6 4.5h4" stroke="#fff" stroke-width="1"/></svg>
  <div class="abs top-bar">Call Us Today! 345.555.0194 &nbsp;|&nbsp; hello@tidalpanecare.ky</div>
  <div class="abs top-divider"></div>

  <div class="abs brand"><span class="brand-mark"></span><span class="brand-name">Tidal Pane Care</span></div>

  <nav class="abs nav" style="left:0;width:960px">
    <a class="current" style="left:491px">Home</a>
    <a style="left:534px">About Us</a>
    <a style="left:588px">Services</a>
    <a style="left:640px">Testimonails</a>
    <a style="left:704px">Contact</a>
    <svg style="position:absolute;left:752px;top:1px" width="7" height="7" viewBox="0 0 10 10" aria-label="Search"><circle cx="4" cy="4" r="3" fill="none" stroke="#333" stroke-width="1.5"/><path d="M6.3 6.3 9 9" stroke="#333" stroke-width="1.6"/></svg>
  </nav>

  <section class="abs hero" role="img" aria-label="Bright living room with a white sofa facing tall clear windows over the blue ocean">
    <h1 class="abs hero-title">Extra services such as ceiling fans cleaning, mirrors, high dusting. Home cleaning services. Power washing.</h1>
    <div class="abs hero-btn">ABOUT US</div>
  </section>

  <h2 class="abs section-title" style="top:273px">About Us</h2>
  <p class="abs section-sub" style="top:304px">Professional. Punctual. In line with your needs</p>
  <div class="abs about-photo" role="img" aria-label="Cleaner wiping a tall window with a squeegee"></div>
  <div class="abs about-copy">
    <p>Tidiness is one of the first things others will notice about you and your surroundings. It doesn't matter whether we speak of the intimate cleanliness of your home… or the impeccable, business-like hygiene of your office. Both are equally important and you should pay huge attention to them.</p>
    <p>Being a family couple, as well as business owners, we fully realize how crucial a sanitary image is both at home and at the workplace. The otherwise classy mirror in your living room, stained by marks you somehow can't scrub off? We have been there. The sting of shame when you invite a client and suddenly notice how hideously unswept your office's window is? We didn't like it either.</p>
  </div>
  <a class="abs read-more">Read more</a>

  <section class="abs consult" role="img" aria-label="Open white window frames looking out on a tropical lagoon with palm trees and a thatched hut">
    <h2 class="abs consult-title">Get Your Free Professional Cleaning Consultation</h2>
    <p class="abs consult-sub">Simply let us know what your needs are and we will get in touch with you!</p>
    <svg class="abs consult-arrow" width="30" height="30" viewBox="0 0 30 30" aria-hidden="true"><circle cx="15" cy="15" r="13.5" fill="none" stroke="#fff" stroke-width="1.8"/><path d="M15 7v15M9 16l6 6 6-6" fill="none" stroke="#fff" stroke-width="1.8"/></svg>
    <form class="abs form-card">
      <div class="field" style="top:9px">Name</div>
      <div class="field" style="top:31px">Mobile Number</div>
      <div class="field" style="top:50px">Email Address</div>
      <div class="field select" style="top:72px">Commercial Window Cleaning</div>
      <div class="field area" style="top:94px">Your Message</div>
      <div class="send-btn" style="left:9px;top:143px">SEND</div>
    </form>
  </section>

  <section class="abs testimonials">
    <h2 class="abs section-title" style="top:22px;width:557px">Client Testimonials</h2>
    <p class="abs section-sub" style="top:53px;width:557px;font-size:9px">Let me say right up front,</p>
    <div class="avatar" style="left:-24px;top:82px;width:70px;height:70px;clip-path:inset(0 0 0 30px)" role="img" aria-label="Client portrait"></div>
    <div class="avatar" style="left:528px;top:82px;width:64px;height:64px;clip-path:inset(0 35px 0 0)" role="img" aria-label="Client portrait"></div>
    <p class="abs quote">If you visited my garage before, you might have ran away screaming. I just do so many things there and it was always so yucky. Not anymore though – with the power washing and custom garage cleaning services of TidalPaneCare, everything's so tidy!!</p>
    <p class="abs quote-role">Teacher</p>
    <p class="abs quote-author">— Marlon Reyes</p>
    <div class="abs quote-bar"></div>
    <div class="slide-btn" style="left:12px;top:103px"></div>
    <div class="slide-btn" style="left:529px;top:103px"></div>
    <div class="dot on" style="left:271px;top:152px"></div>
    <div class="dot" style="left:281px;top:152px"></div>
  </section>

  <div class="abs footer-gap"></div>
  <footer class="abs footer">
    <h3 class="footer-head" style="left:61px">MAIN MENU</h3>
    <h3 class="footer-head" style="left:247px">CONTACT INFO</h3>
    <h3 class="footer-head" style="left:433px">GET IN TOUCH</h3>
    <div class="menu">
      <a class="current" style="top:40px">Home</a>
      <a style="top:61px">About Us</a>
      <a style="top:81px">Services</a>
      <a style="top:102px">Testimonials</a>
      <a style="top:122px">Contact</a>
    </div>
    <div class="abs contact-lines">
      Tidal Pane Care, George Town, Grand Cayman<br>
      Phone: + 345 555 0194<br>
      Mobile: + 345 555 0194<br>
      Fax: + 345 555 0177<br>
      Email: info@tidalpanecare.ky<br>
      Web: tidalpanecare.ky
    </div>
    <div class="foot-field" style="top:40px">Name</div>
    <div class="foot-field" style="top:58px">Email Address</div>
    <div class="foot-field" style="top:78px;height:40px;padding-left:6px">Your Message</div>
    <div class="send-btn" style="left:433px;top:125px;width:48px;height:19px">SEND</div>
  </footer>
  <div class="abs bottom-bar">
    <p class="abs copyright">Copyright 2015 Tidal Pane Care | All Rights Reserved</p>
    <span class="social" style="left:561px" aria-label="Social link"></span>
    <span class="social" style="left:579px" aria-label="Social link"></span>
    <span class="social" style="left:597px" aria-label="Social link"></span>
    <svg class="abs to-top" viewBox="0 0 24 15" aria-label="Back to top"><rect width="24" height="15" rx="2" fill="#1b3a5c"/><path d="M8 9l4-4 4 4" fill="none" stroke="#fff" stroke-width="1.3"/></svg>
  </div>
</body>
</html>
```